New Menu Design Project

Rolling Skillet & Brunch Cottage is a Canadian Franchise Chain that currently has 60+ locations. We are looking for our menu to be modernized and redesigned to keep ahead of current trends
Attached you will find our current menu with photos from our various photoshoots, please use as per needed on the menu as we have some great shots of our products that we would like to showcase, especially our pancakes, waffles, French toast & crepes
Additionally you will find a Sample Menu of what we were thinking but we would like to see what other modern menu designs/creative freedom you can come up with
Please remove all beverages from this menu
Please see below link for all files: https://files.brunchvault-share.net/folders/7K22tpwqrzLmxc0DvA9hSfYbN4eRz3Qw1?usp=share_link

```html
<!DOCTYPE html>
<html lang="en">
<head>
<meta charset="utf-8">
<title>Rolling Skillet &amp; Brunch Cottage – Menu</title>
<link href="https://fonts.googleapis.com/css2?family=Anton&family=Montserrat:wght@400;600;700;800;900&family=Mr+Dafoe&display=swap" rel="stylesheet">
<style>
:root{
  --stage:#a4a4a4;
  --red:#c8161d;
  --red-deep:#8f0d12;
  --yellow:#f8c318;
  --gold:#c9961a;
  --ink:#161616;
  --muted:#4a4a4a;
  --white:#ffffff;
  --pink:#f4d3d3;
}
*{box-sizing:border-box;margin:0;padding:0}
html,body{width:1200px;height:1117px;overflow:hidden;background:var(--stage);font-family:"Montserrat",sans-serif}
.sheet{position:absolute;width:334px;height:471px;background:var(--white);overflow:hidden;box-shadow:0 2px 6px rgba(0,0,0,.25)}
.abs{position:absolute}
.photo{position:absolute;border-radius:6px;background:linear-gradient(135deg,#e9c07a,#b5652c 55%,#6e3218)}
.photo.fresh{background:linear-gradient(135deg,#f6e0b8,#e2553e 50%,#8e1c1c)}
.photo.green{background:linear-gradient(135deg,#c8d98a,#c9803b 55%,#7a3f1a)}
.photo.round{border-radius:50%}
.script{font-family:"Mr Dafoe",cursive;font-weight:400;line-height:.9}
.pill{display:inline-block;font:800 7px/1 "Montserrat",sans-serif;letter-spacing:.3px;padding:3px 12px;border-radius:8px;text-transform:uppercase}
.pill.dark{background:var(--ink);color:var(--white)}
.pill.gold{background:var(--yellow);color:var(--red)}
.intro{font:400 3.5px/1.25 "Montserrat",sans-serif;color:var(--muted);text-align:center;margin:3px 0 4px}
.item{display:flex;justify-content:space-between;gap:4px;font:700 4.3px/1.2 "Montserrat",sans-serif;color:var(--ink)}
.desc{font:400 3.3px/1.22 "Montserrat",sans-serif;color:var(--muted);margin-bottom:2.4px}
.tight .item{margin-bottom:1.6px}
.on-red .item{color:var(--white)}
.on-red .desc,.on-red .intro{color:var(--pink)}
.on-gold .item{color:var(--ink)}
.on-gold .desc,.on-gold .intro{color:#3a2a00}
.brand{display:flex;align-items:center;gap:5px}
.brand-dot{width:16px;height:16px;border-radius:50%;background:var(--yellow);flex:none}
.brand-name{font:800 8px/1.1 "Montserrat",sans-serif;color:var(--yellow)}
.menu-footer{position:absolute;left:0;bottom:0;width:334px;height:50px;background:var(--ink);padding:7px 12px 0}
.legend{display:flex;gap:4px}
.legend-box{display:flex;align-items:center;gap:3px;border:.8px solid var(--white);border-radius:3px;height:15px;padding:0 4px;color:var(--white);font:700 3.2px/1.15 "Montserrat",sans-serif;text-transform:uppercase}
.legend-box.sig{width:64px;font-size:4.6px}
.legend-box.wide{flex:1}
.legend-icon{width:8px;height:8px;border-radius:50%;background:var(--yellow);flex:none}
.legend-icon.sq{border-radius:1px}
.footnote{color:#cfcfcf;font:400 2.9px/1.3 "Montserrat",sans-serif;text-align:center;margin-top:6px}
.cover-top{left:0;top:0;width:334px;height:150px;background:linear-gradient(160deg,#d21b22,#9a0f14)}
.price-hero{font:900 36px/1 "Montserrat",sans-serif;color:var(--white);letter-spacing:-1px}
.breakfast-word{font:400 24px/1 "Anton",sans-serif;color:var(--yellow);letter-spacing:.5px}
.hours{background:var(--ink);color:var(--white);font:800 6px/1 "Montserrat",sans-serif;padding:4px 8px}
.hours b{color:var(--yellow)}
.lunch-panel{left:14px;top:150px;width:320px;height:175px;background:var(--white);border-radius:10px 0 0 10px}
.day{font:600 3.4px/1.1 "Montserrat",sans-serif;color:var(--muted);text-transform:uppercase}
.burger-name{font:800 5px/1.05 "Montserrat",sans-serif;color:var(--red);text-transform:uppercase;margin:1px 0}
.burger-desc{font:400 2.9px/1.2 "Montserrat",sans-serif;color:var(--muted)}
.deal-circle{left:20px;top:240px;width:98px;height:98px;border-radius:50%;background:var(--yellow);border:3px solid var(--white);text-align:center;padding-top:20px}
.deal-price{font:900 27px/1 "Montserrat",sans-serif;color:var(--red)}
.deal-price sup{font-size:11px;vertical-align:top}
.upgrades{left:217px;top:294px;width:117px;height:177px;background:var(--yellow);border-radius:10px 0 0 0;padding:10px 10px 0 12px}
.upgrades .item{color:var(--red-deep);text-transform:uppercase;font-size:4.1px}
.winter{left:14px;top:332px;width:190px;height:84px;background:var(--white);border-radius:8px;padding:8px 8px 0}
.winter-title{font:800 5.4px/1 "Montserrat",sans-serif;color:var(--red);text-align:center;margin-bottom:5px}
.winter-label{font:800 5px/1.2 "Montserrat",sans-serif;color:var(--white);text-align:center;text-transform:uppercase}
.title-tab{background:var(--red);color:var(--white);font:400 34px/1 "Anton",sans-serif;padding:14px 0 0 14px}
</style>
</head>
<body>

<section class="sheet" style="left:80px;top:70px;background:linear-gradient(180deg,var(--red),var(--red-deep))">
  <div class="abs cover-top"></div>
  <div class="abs brand" style="left:20px;top:16px;width:150px">
    <span class="brand-dot"></span>
    <span class="brand-name">Rolling Skillet &amp;<br>Brunch Cottage</span>
  </div>
  <div class="photo round" style="left:10px;top:48px;width:170px;height:90px;border-radius:50% 50% 45% 45%" role="img" aria-label="Breakfast plate with pancakes, eggs, bacon and home fries"></div>
  <div class="abs" style="left:126px;top:60px;font:800 6px/1 Montserrat,sans-serif;color:var(--white)">*DINE-IN ONLY</div>
  <div class="abs price-hero" style="left:200px;top:10px">$6.99</div>
  <div class="abs breakfast-word" style="left:200px;top:50px">BREAKFAST</div>
  <div class="abs script" style="left:192px;top:74px;font-size:40px;color:var(--white)">Special</div>
  <div class="abs hours" style="left:232px;top:124px">MON-FRI <b>7AM-9AM</b></div>

  <div class="abs lunch-panel"></div>
  <div class="abs" style="left:28px;top:158px;width:100px">
    <div style="font:700 6px/1 Montserrat,sans-serif;color:var(--ink);padding-left:40px">Try our</div>
    <div class="script" style="font-size:34px;color:var(--red)">Daily</div>
    <div class="script" style="font-size:28px;color:var(--ink);padding-left:14px">Lunch</div>
    <div style="font:700 7px/1 Montserrat,sans-serif;letter-spacing:3px;color:var(--red);margin-top:4px">Specials</div>
  </div>
  <div class="abs deal-circle">
    <div class="deal-price">$13<sup>.99</sup></div>
    <div style="font:800 4.5px/1 Montserrat,sans-serif;color:var(--red)">+TAX</div>
    <div class="script" style="font-size:28px;color:var(--ink)">Each</div>
  </div>

  <div class="photo round" style="left:132px;top:156px;width:38px;height:38px" role="img" aria-label="Bacon cheddar jalapeño ranch burger"></div>
  <div class="abs" style="left:172px;top:158px;width:40px"><div class="day">Monday</div><div class="burger-name">Bacon Cheddar Jalapeño Ranch Burger</div><div class="burger-desc">Cheddar, bacon, jalapeño &amp; ranch</div></div>
  <div class="photo round" style="left:218px;top:156px;width:38px;height:38px" role="img" aria-label="California burger"></div>
  <div class="abs" style="left:258px;top:158px;width:60px"><div class="day">Tuesday</div><div class="burger-name">California Burger</div><div class="burger-desc">Cheddar, bacon, guac &amp; chipotle mayo</div></div>
  <div class="photo round" style="left:132px;top:205px;width:38px;height:38px" role="img" aria-label="Melt burger"></div>
  <div class="abs" style="left:172px;top:210px;width:40px"><div class="day">Wednesday</div><div class="burger-name">Melt Burger</div><div class="burger-desc">Cheddar, bacon &amp; chipotle mayo</div></div>
  <div class="photo round" style="left:218px;top:205px;width:38px;height:38px" role="img" aria-label="Loaded mushroom burger"></div>
  <div class="abs" style="left:258px;top:206px;width:60px"><div class="day">Thursday</div><div class="burger-name">Loaded Mushroom Burger</div><div class="burger-desc">Swiss, mushrooms, bacon &amp; mayo</div></div>
  <div class="photo round" style="left:132px;top:255px;width:38px;height:38px" role="img" aria-label="BBQ Philly burger"></div>
  <div class="abs" style="left:172px;top:258px;width:40px"><div class="day">Friday</div><div class="burger-name">BBQ Philly Burger</div><div class="burger-desc">Mozza, mushrooms, peppers &amp; crispy onions</div></div>
  <div class="abs" style="left:219px;top:258px;width:108px;height:32px;background:var(--red);border-radius:4px;padding:4px 5px;font:700 3.6px/1.3 Montserrat,sans-serif;color:var(--white)">Served with Broccoli Cheddar or Tomato Chicken Vegetable soup.<br><br>Substitute Soup for Fries or Homefries for $1.00</div>

  <div class="abs upgrades on-gold tight">
    <div class="script" style="font-size:22px;color:var(--ink);text-align:center;margin-bottom:6px">Upgrades</div>
    <div class="item"><span>Onions in Homefries (20 Cals)</span><span>$1.29</span></div>
    <div class="item"><span>Spicy Homefries (40 Cals)</span><span>$1.99</span></div>
    <div class="desc">Spice up your homefries with sautéed onions, peppers and jalapeños</div>
    <div class="item"><span>Holly Homefries (60 Cals)</span><span>$2.99</span></div>
    <div class="desc">Holly up your homefries with hollandaise and cheddar cheese</div>
    <div class="item"><span>Loaded Up Homefries (180 Cals)</span><span>$4.29</span></div>
    <div class="desc">Stack up your homefries with sautéed onions, peppers, bacon bits and cheddar cheese</div>
    <div class="item"><span>Add Flavour (230-1000 Cals)</span><span>$1.99</span></div>
    <div class="desc">Flavour your stack to any of the options under "Signature Stacks"</div>
  </div>

  <div class="abs winter">
    <div class="winter-title">LIMITED TIME ONLY WINTER SPECIALS | $13.99</div>
    <div class="photo fresh" style="left:8px;top:20px;width:54px;height:58px;border-radius:3px" role="img" aria-label="Double chocolate pancakes"></div>
    <div class="photo" style="left:68px;top:20px;width:54px;height:58px;border-radius:3px" role="img" aria-label="Cherry vanilla streusel French toast"></div>
    <div class="photo green" style="left:128px;top:20px;width:54px;height:58px;border-radius:3px" role="img" aria-label="Gingerbread waffle"></div>
  </div>
  <div class="abs winter-label" style="left:22px;top:422px;width:54px">Double Chocolate Cocoa Crunch Pancakes</div>
  <div class="abs winter-label" style="left:82px;top:422px;width:54px">Cherry Vanilla Streusel French Toast</div>
  <div class="abs winter-label" style="left:142px;top:422px;width:54px">Gingerbread Waffle</div>
</section>

<section class="sheet" style="left:433px;top:70px">
  <div class="abs brand" style="left:18px;top:24px;width:140px">
    <span class="brand-dot"></span>
    <span class="brand-name" style="color:var(--red)">Rolling Skillet &amp;<br>Brunch Cottage</span>
  </div>
  <div class="abs title-tab" style="left:163px;top:0;width:171px;height:72px;border-radius:0 0 0 14px">BREAKFAST</div>

  <div class="abs" style="left:16px;top:82px;width:96px">
    <div class="item"><span>Express (710 - 950 Cals)</span><span>$10.79</span></div>
    <div class="desc">2 eggs, choice of bacon, ham, or sausage, served with homefries and Texas toast. Substitute peameal or turkey bacon, add $1.00.</div>
    <div class="item"><span>Jumbo Express (840 - 1220 Cals)</span><span>$12.79</span></div>
    <div class="desc">2 eggs, choice of bacon, ham, or sausage, served with homefries and Texas toast. Substitute peameal, add $1.00.</div>
    <div class="item"><span>Express No-Meat (620 Cals)</span><span>$9.29</span></div>
    <div class="desc">2 eggs served with homefries and Texas toast.</div>
    <div class="item"><span>Farmers Sausage &amp; Eggs (1330 Cals)</span><span>$13.79</span></div>
    <div class="desc">2 eggs with buttered farmers sausage and fried onions. Served with homefries and Texas toast.</div>
  </div>
  <div class="abs" style="left:122px;top:82px;width:96px">
    <div class="item"><span>Steak n' Eggs (1040 Cals)</span><span>$15.99</span></div>
    <div class="desc">6 oz. New York striploin with 3 eggs, homefries and Texas toast.</div>
    <div class="item"><span>Breakfast Wrap (850 Cals)</span><span>$14.69</span></div>
    <div class="desc">3 eggs with your choice of 4 toppings: onions, green peppers, tomatoes, mushrooms, jalapeños, spinach, guacamole, pico salsa, bacon, ham, sausage, cheddar, feta, mozza. Served with homefries.</div>
    <div class="item"><span>The Meatlovers (1230 Cals)</span><span>$15.99</span></div>
    <div class="desc">3 eggs with bacon, ham and sausage. Served with homefries and Texas toast.</div>
    <div class="item"><span>Junior Stack (1030 Cals)</span><span>$12.79</span></div>
    <div class="desc">2 eggs served with 1 bacon, 1 sausage, 1 pancake, homefries and Texas toast.</div>
  </div>
  <div class="abs" style="left:228px;top:82px;width:92px">
    <div class="item"><span>Pancake Stack (1130 Cals)</span><span>$15.79</span></div>
    <div class="desc">2 eggs, choice of bacon, ham or sausage, served with homefries and Texas toast. Substitute peameal, add $1.00.</div>
    <div class="item"><span>Express No-Meat (620 Cals)</span><span>$16.79</span></div>
    <div class="desc">2 eggs served with homefries and Texas toast.</div>
    <div class="item"><span>Farmers Sausage &amp; Eggs (1330 Cals)</span><span>$16.79</span></div>
    <div class="desc">2 eggs with buttered farmers sausage and fried onions. Served with homefries and Texas toast.</div>
    <div class="item"><span>The Meatlovers (1230 Cals)</span><span>$13.79</span></div>
    <div class="desc">3 eggs with bacon, ham and sausage. Served with homefries and Texas toast.</div>
  </div>

  <div class="photo green" style="left:16px;top:215px;width:96px;height:92px" role="img" aria-label="Breakfast hash skillet with eggs"></div>
  <div class="photo fresh" style="left:118px;top:215px;width:96px;height:92px" role="img" aria-label="Waffles with fresh berries"></div>
  <div class="photo" style="left:220px;top:215px;width:98px;height:92px" role="img" aria-label="Eggs benedict plate"></div>

  <div class="abs on-red" style="left:0;top:318px;width:334px;height:104px;background:var(--red)"></div>
  <div class="abs on-red" style="left:14px;top:326px;width:110px">
    <div class="item"><span>Avocado Toast (470 Cals)</span><span>$11.59</span></div>
    <div class="desc">2 pieces of rye toast topped with guacamole, pico salsa and 2 poached medium eggs. Served with fresh fruit.</div>
    <div class="item"><span>G.B.C. Avocado Toast (750 Cals)</span><span>$14.99</span></div>
    <div class="desc">2 pieces of rye toast topped with guacamole, pico salsa, cheddar, bacon and 2 poached medium eggs. Served with your choice of homefries or fresh fruit.</div>
    <div class="item"><span>Veggie Scrambler (570 Cals)</span><span>$11.59</span></div>
    <div class="desc">2 eggs scrambled with onions, green peppers and mushrooms. Served with fresh fruit and Texas toast.</div>
  </div>
  <div class="abs on-gold" style="left:130px;top:318px;width:100px;height:104px;background:var(--yellow);border-radius:8px 0 0 0;padding:8px 8px 0"></div>
  <div class="abs on-gold" style="left:138px;top:326px;width:86px">
    <div class="item"><span>Healthy Start (490 Cals)</span><span>$9.99</span></div>
    <div class="desc">2 poached eggs, fresh fruit and rye toast.</div>
  </div>
  <div class="abs on-red" style="left:128px;top:360px;width:102px;height:62px;background:var(--gold);border-radius:6px;padding:6px 8px">
    <div class="item"><span>Healthy Choice (400 Cals)</span><span>$14.99</span></div>
    <div class="desc">4 egg white omelette with seasoned chicken, guacamole and pico salsa served with turkey bacon and fresh fruit.</div>
  </div>
  <div class="photo fresh" style="left:232px;top:318px;width:102px;height:104px;border-radius:10px 0 0 0" role="img" aria-label="Strawberry topped French toast"></div>

  <footer class="menu-footer">
    <div class="legend">
      <div class="legend-box sig"><span class="legend-icon"></span>Signature Item</div>
      <div class="legend-box wide"><span class="legend-icon sq"></span>Flavour your stack to any of the options under "Signature Stacks" *for $1.99 (235-1000 cals)</div>
      <div class="legend-box wide"><span class="legend-icon sq"></span>Spice up your homefries with sautéed onions, peppers and jalapeños for $1.99 (150 cals)</div>
    </div>
    <p class="footnote">Adults and youth (ages 13 and older) need an average of 2,000 calories a day, and children (ages 4 to 12) need an average of 1,500 calories a day. However, individual needs vary.</p>
  </footer>
</section>

<section class="sheet" style="left:786px;top:70px">
  <div class="photo" style="left:0;top:0;width:170px;height:62px;border-radius:0" role="img" aria-label="Overhead spread of breakfast dishes"></div>
  <div class="abs on-gold" style="left:0;top:60px;width:172px;height:212px;background:var(--yellow);border-radius:0 0 14px 0"></div>
  <div class="abs on-gold" style="left:12px;top:66px;width:148px">
    <div style="text-align:center"><span class="pill dark">Skillet Hash's</span></div>
    <p class="intro">Topped with 2 eggs, tossed with homefries and served with Texas toast.</p>
    <div class="item"><span>Bacon Cheeseburger Hash (1630 Cals)</span><span>$17.89</span></div>
    <div class="desc">Fresh guacamole and pico salsa topped with chipotle mayo and cheddar.</div>
    <div class="item"><span>Mexican Hash (1060 Cals)</span><span>$16.79</span></div>
    <div class="desc">Sausage, peppers, onions, mozza, buffalo sauce, guacamole and pico salsa.</div>
    <div class="item"><span>Cowboy Hash (1080 Cals)</span><span>$16.79</span></div>
    <div class="desc">Bacon, ham, sausage, peppers, onions, cheddar and BBQ sauce.</div>
    <div class="item"><span>Canadian Hash (1260 Cals)</span><span>$16.79</span></div>
    <div class="desc">Maple bacon, peameal, mushrooms and cheddar.</div>
    <div class="item"><span>Benedict Hash (1250 Cals)</span><span>$16.79</span></div>
    <div class="desc">Peameal, cheddar and hollandaise sauce.</div>
    <div class="item"><span>Veggie Hash (970 Cals)</span><span>$16.79</span></div>
    <div class="desc">Mushrooms, tomatoes, onions, green peppers, spinach, served with guacamole and pico salsa.</div>
    <div class="item"><span>Skillet Hash (1120 Cals)</span><span>$17.89</span></div>
    <div class="desc">Sautéed onions and green peppers topped with shaved corned beef, hollandaise and mozza.</div>
    <div class="item"><span>Pulled Pork Hash (1390 Cals)</span><span>$18.89</span></div>
    <div class="desc">Marinated pulled pork, mozza, buffalo ranch, pico salsa and crispy onions.</div>
  </div>

  <div class="abs on-red" style="left:172px;top:0;width:162px;height:421px;background:var(--red)"></div>
  <div class="abs on-red" style="left:182px;top:12px;width:142px">
    <div style="text-align:center"><span class="pill gold">Skillet Omelettes</span></div>
    <p class="intro" style="text-align:left">Served with homefries &amp; Texas toast. Substitute egg whites, add $1.99.</p>
    <div class="item"><span>Western (660 Cals)</span><span>$12.79</span></div><div class="desc">Ham and onions.</div>
    <div class="item"><span>Deluxe Western (850 Cals)</span><span>$13.89</span></div><div class="desc">Ham, onions, peppers and cheddar.</div>
    <div class="item"><span>Vegetarian (690 Cals)</span><span>$13.89</span></div><div class="desc">Mushrooms, peppers, onions and tomatoes.</div>
    <div class="item"><span>Mexican (930 Cals)</span><span>$14.99</span></div><div class="desc">Sausage, peppers, onions, mozza, buffalo sauce, guacamole and pico salsa.</div>
    <div class="item"><span>Spinach Florentine (920 Cals)</span><span>$14.99</span></div><div class="desc">Spinach, mushrooms, onions, mozza, topped with hollandaise and tomatoes.</div>
    <div class="item"><span>Great Canadian (880 Cals)</span><span>$13.89</span></div><div class="desc">Bacon, ham, mushrooms and cheddar.</div>
    <div class="item"><span>Homestyle (930 Cals)</span><span>$14.99</span></div><div class="desc">Bacon, ham, sausage, onions, peppers and cheddar.</div>
    <div class="item"><span>Greek (780 Cals)</span><span>$13.89</span></div><div class="desc">Onions, tomatoes, peppers and feta.</div>
    <div class="item"><span>Meatlovers (930 Cals)</span><span>$13.89</span></div><div class="desc">Bacon, ham, sausage and cheddar.</div>
    <div class="item"><span>Spinach (790 Cals)</span><span>$14.99</span></div><div class="desc">Spinach, feta, tomatoes, mushrooms, peppers and onions.</div>
    <div class="item"><span>Build Your Own (665-990 Cals)</span><span>$14.99</span></div><div class="desc">3 eggs with your choice of 4 toppings: onions, green peppers, tomatoes, mushrooms, jalapeños, spinach, guacamole, pico salsa, bacon, ham, sausage, cheddar, mozza, feta or BBQ sauce.</div>
  </div>
  <div class="photo" style="left:178px;top:244px;width:156px;height:94px;border-radius:10px 0 0 10px" role="img" aria-label="Sunny side up eggs with hash"></div>
  <div class="photo fresh" style="left:178px;top:344px;width:156px;height:77px;border-radius:10px 0 0 0" role="img" aria-label="Eggs, bacon and toast breakfast"></div>

  <div class="abs" style="left:12px;top:280px;width:152px">
    <div class="script" style="font-size:26px;color:var(--red);text-align:center">Eggs Benedict</div>
    <p class="intro">Served with homefries, fresh fruit and topped with cheese garnish.</p>
    <div class="tight" style="padding:0 8px">
      <div class="item"><span>Bacon Benedict (840 Cals)</span><span>$14.79</span></div>
      <div class="item"><span>Ham Benedict (700 Cals)</span><span>$14.79</span></div>
      <div class="item"><span>Peameal Benedict</span><span>$14.79</span></div>
      <div class="item"><span>Turkey Bacon Benedict</span><span>$14.79</span></div>
      <div class="item"><span>Peameal &amp; Spinach (820 Cals)</span><span>$15.79</span></div>
      <div class="item"><span>Spinach &amp; Mushroom (650 Cals)</span><span>$15.79</span></div>
      <div class="item"><span>Southwest Benedict (720 Cals)</span><span>$15.79</span></div>
      <div class="desc">Fresh guacamole and pico salsa topped with chipotle mayo and cheddar.</div>
      <div class="item"><span>Pulled Pork &amp; Mozza Benedict (920 Cals)</span><span>$17.99</span></div>
      <div class="desc">Marinated pulled pork topped with buffalo ranch and mozza.</div>
    </div>
  </div>

  <footer class="menu-footer">
    <div class="legend">
      <div class="legend-box sig"><span class="legend-icon"></span>Signature Item</div>
      <div class="legend-box wide"><span class="legend-icon sq"></span>Flavour your stack to any of the options under "Signature Stacks" *for $1.99 (235-1000 cals)</div>
      <div class="legend-box wide"><span class="legend-icon sq"></span>Spice up your homefries with sautéed onions, peppers and jalapeños for $1.99 (150 cals)</div>
    </div>
    <p class="footnote">Adults and youth (ages 13 and older) need an average of 2,000 calories a day, and children (ages 4 to 12) need an average of 1,500 calories a day. However, individual needs vary.</p>
  </footer>
</section>

<section class="sheet" style="left:80px;top:563px">
  <div class="photo" style="left:0;top:0;width:168px;height:92px;border-radius:0" role="img" aria-label="Chocolate pancakes with whipped cream"></div>
  <div class="abs" style="left:176px;top:14px;width:148px">
    <div style="text-align:center"><span class="pill dark">Brunch <span style="color:var(--yellow)">Sandwiches</span></span></div>
    <p class="intro">Served with fries, homefries or homemade soup.</p>
    <div class="item"><span>Shaved Ham &amp; Egg Melt (700 Cals)</span><span>$13.99</span></div><div class="desc">Shaved ham smothered with mozza, cheddar, scrambled eggs, grilled on rye.</div>
    <div class="item"><span>Avocado Brunch Sandwich (970 Cals)</span><span>$13.99</span></div><div class="desc">Scrambled eggs, guacamole, mozza, lettuce, tomato and chipotle mayo on rye.</div>
    <div class="item"><span>Toasted Denver (830 Cals)</span><span>$13.99</span></div><div class="desc">Scrambled eggs mixed with ham, onions, tomatoes and peppers topped with cheddar and chipotle mayo.</div>
    <div class="item"><span>Monte Cristo (670 Cals)</span><span>$13.99</span></div><div class="desc">French toast stuffed with ham and mozza.</div>
    <div class="item"><span>The C-Belt (880 Cals)</span><span>$14.99</span></div><div class="desc">Triple decker with cheddar, bacon, egg, lettuce, tomato and mayo.</div>
    <div class="tight">
      <div class="item"><span>Shaved Ham &amp; Egg Melt (700 Cals)</span><span>$11.59</span></div>
      <div class="item"><span>Western (620 Cals)</span><span>$11.59</span></div>
      <div class="item"><span>Grilled Cheese w/Bacon (790 Cals)</span><span>$11.59</span></div>
      <div class="item"><span>BLT (770 Cals)</span><span>$11.59</span></div>
    </div>
  </div>

  <div class="abs on-red" style="left:0;top:80px;width:170px;height:246px;background:var(--red);border-radius:0 14px 14px 0"></div>
  <div class="abs on-red" style="left:16px;top:88px;width:144px">
    <div style="text-align:center"><span class="pill gold">Signature Stacks</span></div>
    <p class="intro">Topped with whipped cream.</p>
    <div class="tight">
      <div class="item"><span>Pancakes (700 Cals)</span><span>$10.49</span></div>
      <div class="item"><span>Gluten-Friendly Pancakes (1170 Cals)</span><span>$12.49</span></div>
      <div class="item"><span>Chocolate Chip (650 Cals)</span><span>$11.99</span></div>
      <div class="item"><span>Blueberry (780 Cals)</span><span>$12.49</span></div>
      <div class="item"><span>Simply Strawberries (730 Cals)</span><span>$12.49</span></div>
      <div class="item"><span>Strawberry Banana (840 Cals)</span><span>$13.49</span></div>
      <div class="item"><span>Chocolate Banana (960 Cals)</span><span>$12.99</span></div>
      <div class="item"><span>Blueberry Banana (890 Cals)</span><span>$13.49</span></div>
      <div class="item"><span>Hazelnut Strawberry (1070 Cals)</span><span>$13.99</span></div>
      <div class="item"><span>NY Strawberry Cheesecake (1160 Cals)</span><span>$14.49</span></div>
    </div>
    <div class="desc">Topped with fresh strawberries, cream cheese icing, strawberry preserve and graham crumbs.</div>
    <div class="item"><span>NY Blueberry Cheesecake (1050 Cals)</span><span>$14.49</span></div>
    <div class="desc">Topped with fresh blueberries, cream cheese icing, blueberry preserve and graham crumbs.</div>
    <div class="item"><span>Cookies &amp; Cream (980 Cals)</span><span>$13.99</span></div>
    <div class="desc">Stuffed and topped with crushed cookies &amp; vanilla icing.</div>
    <div class="item"><span>Cinnamon Bun Cakes (1430 Cals)</span><span>$13.99</span></div>
    <div class="desc">Our signature pancakes filled with cinnamon bun filling topped with a cream cheese icing.</div>
    <div class="tight">
      <div class="item"><span>Birthday Cake (1080 Cals)</span><span>$10.49</span></div>
      <div class="item"><span>Chocolate Chip Cookie Dough (1150 Cals)</span><span>$12.49</span></div>
      <div class="item"><span>Chocolate Caramel Brownie (1290 Cals)</span><span>$11.99</span></div>
    </div>
  </div>
  <div class="photo fresh" style="left:174px;top:196px;width:160px;height:140px;border-radius:12px 0 0 12px" role="img" aria-label="Strawberry pancakes with fruit salad"></div>

  <div class="abs" style="left:22px;top:335px;width:14px;height:80px;background:var(--yellow);border-radius:7px"></div>
  <div class="abs" style="left:8px;top:368px;width:42px;transform:rotate(-90deg);font:900 7px/1 Montserrat,sans-serif;color:var(--ink);text-align:center">SIDES</div>
  <div class="abs tight" style="left:52px;top:340px;width:90px">
    <div class="item"><span>Bacon (260 Cals)</span><span>$3.99</span></div>
    <div class="item"><span>Ham (90 Cals)</span><span>$3.99</span></div>
    <div class="item"><span>Sausage (440 Cals)</span><span>$3.99</span></div>
    <div class="item"><span>Peameal (270 Cals)</span><span>$4.99</span></div>
    <div class="item"><span>Turkey Bacon (140 Cals)</span><span>$4.99</span></div>
    <div class="item"><span>Extra Egg (70 Cals)</span><span>$1.99</span></div>
    <div class="item"><span>Fresh Fruit (60 Cals)</span><span>$3.99</span></div>
    <div class="item"><span>Homefries (170 Cals)</span><span>$4.49</span></div>
    <div class="item"><span>French Fries (290 Cals)</span><span>$4.49</span></div>
  </div>
  <div class="abs tight" style="left:158px;top:340px;width:120px">
    <div class="item"><span>Hollandaise (160 Cals)</span><span>$3.49</span></div>
    <div class="item"><span>Pure Canadian Maple Syrup (80 Cals)</span><span>$1.49</span></div>
    <div class="item"><span>Fresh Homemade Soup (190-300 Cals)</span><span>$4.99</span></div>
    <div class="item"><span>Fresh Homemade Soup (190-300 Cals)</span><span>$1.79</span></div>
    <div class="item"><span>Side 1 French Toast (240 Cals)</span><span>$3.99</span></div>
    <div class="item"><span>Side 1 Pancake (240 Cals)</span><span>$3.99</span></div>
    <div class="item"><span>Side Farmers Sausage (780 Cals)</span><span>$5.99</span></div>
    <div class="item"><span>Toast N' Jam (300 Cals)</span><span>$2.99</span></div>
  </div>

  <footer class="menu-footer">
    <div class="legend">
      <div class="legend-box sig"><span class="legend-icon"></span>Signature Item</div>
      <div class="legend-box wide"><span class="legend-icon sq"></span>Flavour your stack to any of the options under "Signature Stacks" *for $1.99 (235-1000 cals)</div>
      <div class="legend-box wide"><span class="legend-icon sq"></span>Spice up your homefries with sautéed onions, peppers and jalapeños for $1.99 (150 cals)</div>
    </div>
    <p class="footnote">Adults and youth (ages 13 and older) need an average of 2,000 calories a day, and children (ages 4 to 12) need an average of 1,500 calories a day. However, individual needs vary.</p>
  </footer>
</section>

<section class="sheet" style="left:433px;top:563px">
  <div class="photo green" style="left:0;top:0;width:162px;height:106px;border-radius:0 0 12px 0" role="img" aria-label="Salad topped with crispy onions"></div>
  <div class="abs on-gold" style="left:166px;top:0;width:168px;height:210px;background:var(--yellow);border-radius:0 0 0 14px"></div>
  <div class="abs on-gold" style="left:176px;top:14px;width:148px">
    <div style="text-align:center"><span class="pill dark">French Toast</span></div>
    <p class="intro">Topped with whipped cream and cinnamon.</p>
    <div class="tight">
      <div class="item"><span>French Toast (700 Cals)</span><span>$10.49</span></div>
      <div class="item"><span>Gluten-Friendly French Toast (760 Cals)</span><span>$12.49</span></div>
      <div class="item"><span>Simply Strawberries (730 Cals)</span><span>$12.99</span></div>
      <div class="item"><span>Strawberry Banana (840 Cals)</span><span>$13.99</span></div>
      <div class="item"><span>Hazelnut Banana (870 Cals)</span><span>$13.99</span></div>
      <div class="item"><span>Strawberry Blueberry (740 Cals)</span><span>$14.49</span></div>
      <div class="item"><span>Cookies &amp; Cream (980 Cals)</span><span>$13.99</span></div>
    </div>
    <div class="desc">Topped with crushed cookies and vanilla icing.</div>
    <div class="item"><span>NY Strawberry Cheesecake (1160 Cals)</span><span>$14.99</span></div>
    <div class="desc">Topped with fresh strawberries, cream cheese icing, strawberry preserve and graham crumbs.</div>
    <div class="item"><span>Berries &amp; Cream (1140 Cals)</span><span>$14.99</span></div>
    <div class="desc">Topped with fresh strawberries, blueberries, cream cheese icing, strawberry and blueberry preserve.</div>
    <div class="item"><span>Strawberry Banana Hazelnut Cream (1230 Cals)</span><span>$14.99</span></div>
    <div class="desc">Topped with fresh strawberries, bananas, hazelnut and cream cheese icing.</div>
    <div class="item"><span>Banana Bread French Toast (1440 Cals)</span><span>$15.99</span></div>
    <div class="desc">Banana bread topped with bananas and cream cheese icing.</div>
  </div>

  <div class="abs" style="left:14px;top:112px;width:146px">
    <div style="text-align:center"><span class="pill dark">Salads</span></div>
    <p class="intro">Served with your choice of fries, soup or salad.</p>
    <div class="item"><span>Grilled Chicken Caesar Salad (660 Cals)</span><span>$15.99</span></div>
    <div class="desc">Romaine, bacon, parmesan cheese tossed in a creamy caesar dressing, topped with croutons &amp; seasoned grilled chicken. Side not incl.</div>
    <div class="item"><span>Mexican Cobb Salad (460 Cals)</span><span>$16.99</span></div>
    <div class="desc">Romaine, bacon, cheddar &amp; mozza in a buffalo ranch dressing, topped with pico salsa, guacamole, crispy onions &amp; seasoned grilled chicken. Side not incl.</div>
  </div>

  <div class="abs on-gold" style="left:0;top:200px;width:172px;height:104px;background:var(--yellow);border-radius:0 14px 14px 0"></div>
  <div class="abs on-gold" style="left:14px;top:208px;width:146px">
    <div style="text-align:center"><span class="pill" style="background:var(--white);color:var(--red)">Crepes</span></div>
    <p class="intro">Served with your choice of homefries or fresh fruit.</p>
    <div class="item"><span>Spinach Florentine Crepes (870 Cals)</span><span>$14.49</span></div>
    <div class="desc">2 crepes stuffed with eggs, spinach, mushrooms, onions and mozza. Topped with hollandaise and pico salsa.</div>
    <div class="item"><span>Banana Berry Crepes (910 Cals)</span><span>$13.99</span></div>
    <div class="desc">2 crepes stuffed with hazelnut and bananas, topped with fresh strawberries and a light chocolate drizzle.</div>
    <div class="item"><span>Strawberry Vanilla (880 Cals)</span><span>$13.99</span></div>
    <div class="desc">2 crepes stuffed with strawberry preserve and bananas, topped with vanilla icing &amp; fresh strawberries.</div>
  </div>
  <div class="photo fresh" style="left:0;top:308px;width:164px;height:113px;border-radius:0 12px 0 0" role="img" aria-label="Strawberry pancake stack with cream"></div>
  <div class="photo" style="left:180px;top:210px;width:154px;height:70px;border-radius:10px 0 0 10px" role="img" aria-label="Waffles with blueberries and cream"></div>

  <div class="abs" style="left:180px;top:284px;width:144px">
    <div style="display:flex;align-items:baseline;gap:4px;padding-left:6px"><span class="script" style="font-size:26px;color:var(--red)">Waffles</span><span class="intro" style="text-align:left;margin:0">Topped with<br>whipped cream.</span></div>
    <div class="tight" style="margin-top:2px">
      <div class="item"><span>Waffle (640 Cals)</span><span>$10.49</span></div>
      <div class="item"><span>Gluten-Friendly Waffle (610 Cals)</span><span>$12.49</span></div>
      <div class="item"><span>Simply Strawberries (670 Cals)</span><span>$12.99</span></div>
      <div class="item"><span>Blueberry Banana (830 Cals)</span><span>$13.49</span></div>
      <div class="item"><span>Strawberry Banana (780 Cals)</span><span>$13.99</span></div>
      <div class="item"><span>Strawberry Blueberry (720 Cals)</span><span>$14.49</span></div>
      <div class="item"><span>Fresh Fruit (750 Cals)</span><span>$15.49</span></div>
      <div class="item"><span>Hazelnut Strawberries &amp; Cream (1020 Cals)</span><span>$14.99</span></div>
    </div>
    <div class="desc">Topped with fresh strawberries, hazelnut and cream cheese icing.</div>
    <div class="item"><span>Cookies &amp; Cream (920 Cals)</span><span>$14.49</span></div>
    <div class="desc">Stuffed and topped with crushed cookies &amp; vanilla icing.</div>
  </div>

  <footer class="menu-footer">
    <div class="legend">
      <div class="legend-box sig"><span class="legend-icon"></span>Signature Item</div>
      <div class="legend-box wide"><span class="legend-icon sq"></span>Flavour your stack to any of the options under "Signature Stacks" *for $1.99 (235-1000 cals)</div>
      <div class="legend-box wide"><span class="legend-icon sq"></span>Spice up your homefries with sautéed onions, peppers and jalapeños for $1.99 (150 cals)</div>
    </div>
    <p class="footnote">Adults and youth (ages 13 and older) need an average of 2,000 calories a day, and children (ages 4 to 12) need an average of 1,500 calories a day. However, individual needs vary.</p>
  </footer>
</section>

<section class="sheet" style="left:786px;top:563px">
  <div class="abs" style="left:12px;top:10px;width:150px">
    <div style="display:flex;align-items:flex-end;justify-content:center;gap:3px"><span class="script" style="font-size:32px;color:var(--red)">Lunches</span><span class="intro" style="text-align:left;margin:0 0 3px">served with your choice<br>of fries, homefries or soup.</span></div>
    <div style="margin-top:6px">
      <div class="item"><span>Skillet Club (1000 - 1200 Cals)</span><span>$17.99</span></div><div class="desc">Triple decker with chicken, ham, bacon, lettuce, tomato, cheddar and mayo.</div>
      <div class="item"><span>Southwest Chicken Sandwich (900 - 1050 Cals)</span><span>$15.99</span></div><div class="desc">Seasoned grilled chicken, cheddar, guacamole, frizzled onions and chipotle mayo served on a bun.</div>
      <div class="item"><span>Peameal &amp; Cheddar Melt on a Bun (750 - 950 Cals)</span><span>$14.99</span></div><div class="desc">Peameal, cheddar, lettuce, tomato and mayo on a bun.</div>
      <div class="item"><span>Original Reuben (580 - 750 Cals)</span><span>$15.99</span></div><div class="desc">Smoked corned beef, mozza, sauerkraut and mustard grilled on rye.</div>
      <div class="item"><span>Chicken Club (900 - 1050 Cals)</span><span>$16.99</span></div><div class="desc">Seasoned grilled chicken, cheddar, peameal, lettuce, tomato and chipotle mayo on a bun.</div>
      <div class="item"><span>Chicken Fingers (100 - 140 Cals)</span><span>$15.99</span></div><div class="desc">Golden brown fillets of seasoned chicken breast with fries. Get them sauced and tossed! Your choice of BBQ or buffalo, add $1.00.</div>
      <div class="item"><span>Pulled Pork Grilled Cheese (810 Cals)</span><span>$14.99</span></div><div class="desc">Marinated pulled pork, cheddar, mozza, caramelized onions and buffalo ranch.</div>
      <div class="item"><span>Veggie Grilled Cheese (900 Cals)</span><span>$12.99</span></div><div class="desc">Cheddar, mozza, onions, peppers, jalapeños, sliced tomatoes and chipotle mayo.</div>
    </div>
  </div>

  <div class="photo" style="left:168px;top:0;width:166px;height:86px;border-radius:0 0 0 12px" role="img" aria-label="Stacked burger with bacon and cheese"></div>
  <div class="abs on-red" style="left:168px;top:82px;width:166px;height:226px;background:var(--red);border-radius:14px 0 0 14px"></div>
  <div class="abs on-red" style="left:178px;top:92px;width:146px">
    <div style="text-align:center"><span class="pill gold">Burgers &amp; Wraps</span></div>
    <p class="intro">Fresh burgers made in-house sprinkled with lettuce, tomatoes, and red onions. Served with fries, homefries or soup.</p>
    <div class="item"><span>Country Burger (900 - 1030 Cals)</span><span>$13.99</span></div><div class="desc">Comes plain, feel free to top it any way you would like. Add cheese for only $1.00.</div>
    <div class="item"><span>Banquet Burger (1090 - 1220 Cals)</span><span>$15.99</span></div><div class="desc">Topped with bacon and cheddar.</div>
    <div class="item"><span>Chipotle Breakfast Burger (1180 - 1310 Cals)</span><span>$14.99</span></div><div class="desc">Our medium egg, peameal and cheddar topped with chipotle mayo.</div>
    <div class="item"><span>BBQ Cowboy Burger (1150 - 1280 Cals)</span><span>$15.99</span></div><div class="desc">Bacon, cheddar and frizzled onions topped with BBQ sauce.</div>
    <div class="item"><span>Skillet Burger (1350 - 1480 Cals)</span><span>$16.99</span></div><div class="desc">2 crispy chicken fingers on a beef patty topped with cheddar and bacon.</div>
    <div class="item"><span>Crispy Chicken Caesar Wrap (930 - 1060 Cals)</span><span>$15.99</span></div><div class="desc">Crispy chicken, romaine, bacon and parmesan cheese tossed in creamy caesar dressing.</div>
    <div class="item"><span>Buffalo Chicken &amp; Bacon Ranch Wrap (930 - 1060 Cals)</span><span>$14.99</span></div><div class="desc">Crispy chicken, bacon, cheddar, romaine and tomatoes tossed in buffalo ranch.</div>
    <div class="item"><span>Chipotle Chicken &amp; Guac Wrap (900 - 1030 Cals)</span><span>$12.99</span></div><div class="desc">Seasoned chicken, bacon, cheddar, guacamole, romaine and pico salsa, tossed in chipotle mayo.</div>
  </div>

  <div class="photo green" style="left:14px;top:218px;width:144px;height:86px;border-radius:8px" role="img" aria-label="Club sandwich with fries"></div>

  <div class="abs on-gold" style="left:0;top:310px;width:172px;height:111px;background:var(--yellow);border-radius:0 14px 0 0"></div>
  <div class="abs on-gold" style="left:14px;top:318px;width:146px">
    <div style="text-align:center"><span class="pill dark">Poutines</span></div>
    <div style="margin-top:5px">
      <div class="item"><span>Buffalo Chicken Poutine (990 Cals)</span><span>$15.99</span></div><div class="desc">Crispy chicken, bacon, mozza, gravy topped with buffalo sauce.</div>
      <div class="item"><span>Chicken &amp; Bacon Poutine (1150 Cals)</span><span>$16.99</span></div><div class="desc">Crispy chicken, bacon, cheddar, tomato, gravy topped with caesar sauce.</div>
      <div class="item"><span>Classic Poutine (740 Cals)</span><span>$15.99</span></div><div class="desc">Mozza, cheddar and gravy.</div>
      <div class="item"><span>Pulled Pork Poutine (1130 Cals)</span><span>$16.99</span></div><div class="desc">Marinated pulled pork, bacon, mozza, gravy topped with buffalo ranch.</div>
    </div>
  </div>
  <div class="photo" style="left:176px;top:310px;width:158px;height:111px;border-radius:12px 0 0 0" role="img" aria-label="Reuben sandwich with fries"></div>

  <footer class="menu-footer">
    <div class="legend">
      <div class="legend-box sig"><span class="legend-icon"></span>Signature Item</div>
      <div class="legend-box wide"><span class="legend-icon sq"></span>Flavour your stack to any of the options under "Signature Stacks" *for $1.99 (235-1000 cals)</div>
      <div class="legend-box wide"><span class="legend-icon sq"></span>Spice up your homefries with sautéed onions, peppers and jalapeños for $1.99 (150 cals)</div>
    </div>
    <p class="footnote">Adults and youth (ages 13 and older) need an average of 2,000 calories a day, and children (ages 4 to 12) need an average of 1,500 calories a day. However, individual needs vary.</p>
  </footer>
</section>

</body>
</html>
```